Business Card Design for Small Electrical Contractor

I need to update my business card into something a little more modern. We are a small electrical contracting company. We service domestic and commercial places around Sydney. We have 2 logo designs at the moment. I have uploaded both and 2 different sizes to work with.

Industry/Entity Type

Business

Contact Information for Business Card

Leo Hartigan
8/21-23 Birch Rd, Kelsworth 2087
t - (02) 9381 4720
m - 0427 815 903
E - info@hartiganelx.com.au
W - hartiganelx.com.au
ABN: 42 907 551 316

Font styles to use
Sans Serif

Requirements
Must have
• I would also like to see the below fit on somewhere aswell
• - Licensed Electrician
• - Level 2 (Cat 1 & 4)
• - Domestic
• - Commercial
• - Repairs and Installations
• - Data
Nice to have
• Try and keep similar colours as logo
Should not have
• No lightning bolts or light globes. Smart and professional please.

```html
<!DOCTYPE html>
<html lang="en">
<head>
<meta charset="utf-8">
<title>Hartigan Electrical – Business Card</title>
<link rel="stylesheet" href="https://fonts.googleapis.com/css2?family=Source+Sans+3:wght@400;600&family=Tinos&display=swap">
<style>
  :root {
    --ink: #000000;
    --paper: #ffffff;
    --orange: #ff8412;
    --icon-bg: #fdbb3a;
    --brand-green: #0e3b2e;
    --text-dark: #111111;
    --sans: "Source Sans 3", Arial, sans-serif;
    --serif: "Tinos", "Times New Roman", serif;
  }
  * { box-sizing: border-box; margin: 0; padding: 0; }
  html, body { width: 1131px; height: 1200px; overflow: hidden; background: var(--paper); }
  .canvas { position: relative; width: 1131px; height: 1200px; }

  /* Front of card */
  .card-front {
    position: absolute; left: 67px; top: 0; width: 1002px; height: 577px;
    background: var(--ink); border-radius: 40px; overflow: hidden;
  }
  .card-front .accent-band {
    position: absolute; left: 0; bottom: 0; width: 100%; height: 58px; background: var(--orange);
  }
  .front-brand {
    position: absolute; left: 241px; top: 202px; width: 518px; height: 172px;
    background: #0a0a0a; display: flex; align-items: center; justify-content: center; gap: 18px;
  }
  .brand-name {
    font-family: var(--sans); font-weight: 600; font-size: 46px; letter-spacing: 1px; white-space: nowrap;
  }
  .front-brand .brand-name { color: var(--paper); }
  .brand-mark { width: 22px; height: 22px; background: var(--orange); flex: none; }

  /* Back of card */
  .card-back {
    position: absolute; left: 67px; top: 600px; width: 1002px; height: 577px;
    border: 1px solid #222; border-radius: 40px; overflow: hidden; background: var(--paper);
  }
  .back-brand {
    position: absolute; left: 99px; top: 740px; transform: translateY(-50%);
    display: flex; align-items: center; gap: 16px; margin-top: -600px;
  }
  .back-brand .brand-name { color: var(--brand-green); font-size: 44px; }

  .contact-list { position: absolute; left: 650px; top: 41px; }
  .contact-item { position: absolute; left: 0; display: flex; align-items: flex-start; gap: 19px; }
  .contact-item:nth-child(1) { top: 0; }
  .contact-item:nth-child(2) { top: 93px; }
  .contact-item:nth-child(3) { top: 184px; }
  .contact-icon {
    width: 51px; height: 51px; border-radius: 5px; background: var(--icon-bg);
    display: flex; align-items: center; justify-content: center; flex: none;
  }
  .contact-text {
    font-family: var(--sans); font-size: 19px; line-height: 26px; color: var(--text-dark); padding-top: 0;
    white-space: nowrap;
  }

  .orange-rule { position: absolute; left: 0; top: 314px; width: 100%; height: 10px; background: var(--orange); }
  .dark-panel { position: absolute; left: 0; top: 324px; width: 100%; height: 253px; background: var(--ink); }

  .holder { position: absolute; left: 50px; top: 400px; color: var(--paper); }
  .holder-name { font-family: var(--serif); font-size: 74px; line-height: 1; letter-spacing: 0.5px; white-space: nowrap; }
  .holder-title {
    font-family: var(--serif); font-size: 21px; letter-spacing: 9.6px; margin-top: 8px; white-space: nowrap;
  }

  .services {
    position: absolute; right: 48px; top: 374px; list-style: none; text-align: right;
    font-family: var(--sans); font-size: 26px; line-height: 32.5px; color: var(--paper);
  }
  .services li::after { content: " •"; font-size: 20px; }

  .abn {
    position: absolute; left: 51px; top: 542px; font-family: var(--sans); font-size: 21px; color: var(--paper);
  }
</style>
</head>
<body>
<div class="canvas">

  <section class="card-front">
    <div class="front-brand">
      <span class="brand-mark"></span>
      <span class="brand-name">Hartigan Electrical</span>
    </div>
    <div class="accent-band"></div>
  </section>

  <section class="card-back">
    <div class="back-brand" style="top:740px;">
      <span class="brand-mark"></span>
      <span class="brand-name">Hartigan Electrical</span>
    </div>

    <div class="contact-list">
      <div class="contact-item">
        <span class="contact-icon">
          <svg width="30" height="30" viewBox="0 0 24 24" aria-hidden="true">
            <path fill="#fff" d="M6.6 10.8a15.1 15.1 0 0 0 6.6 6.6l2.2-2.2a1 1 0 0 1 1-.25 11.4 11.4 0 0 0 3.6.57 1 1 0 0 1 1 1V20a1 1 0 0 1-1 1A17 17 0 0 1 3 4a1 1 0 0 1 1-1h3.5a1 1 0 0 1 1 1c0 1.25.2 2.45.57 3.57a1 1 0 0 1-.25 1z"/>
          </svg>
        </span>
        <p class="contact-text">(02) 9381 4720<br>0427 815 903</p>
      </div>
      <div class="contact-item">
        <span class="contact-icon">
          <svg width="32" height="32" viewBox="0 0 24 24" fill="none" stroke="#fff" stroke-width="1.5" aria-hidden="true">
            <circle cx="12" cy="12" r="9"/>
            <ellipse cx="12" cy="12" rx="4" ry="9"/>
            <path d="M3 12h18M4.5 7.5h15M4.5 16.5h15"/>
          </svg>
        </span>
        <p class="contact-text">info@hartiganelx.com.au<br>hartiganelx.com.au</p>
      </div>
      <div class="contact-item">
        <span class="contact-icon">
          <svg width="30" height="30" viewBox="0 0 24 24" aria-hidden="true">
            <path fill="#fff" d="M12 2a7 7 0 0 0-7 7c0 5.2 7 13 7 13s7-7.8 7-13a7 7 0 0 0-7-7zm0 9.5a2.5 2.5 0 1 1 0-5 2.5 2.5 0 0 1 0 5z"/>
          </svg>
        </span>
        <p class="contact-text">8/21-23 Birch Rd<br>Kelsworth 2087</p>
      </div>
    </div>

    <div class="orange-rule"></div>
    <div class="dark-panel"></div>

    <div class="holder">
      <h1 class="holder-name">Leo Hartigan</h1>
      <p class="holder-title">LICENSED ELECTRICIAN</p>
    </div>

    <ul class="services">
      <li>Level 2 (Cat 1 &amp; 4)</li>
      <li>Domestic</li>
      <li>Commercial</li>
      <li>Repairs and Installations</li>
      <li>Data</li>
    </ul>

    <p class="abn">ABN: 42 907 551 316</p>
  </section>

</div>
</body>
</html>
```